MOLT - Monitoring Natural Hazards from Space Web Application

KORVEN Sarl is a Luxembourg based Space-Startup that works in the field of Earth Observation. KORVEN is a platform able to extract value-added information from satellite data and is specialized in mapping Natural Disaster (floods, fires etc).

We are now developing a new vertical tool, called MOLT, dedicated to the monitoring of natural hazards in Humanitarian Camps around the world.

The goal of MOLT is to hide to the users' all the complexity of the Satellite Image processing and just provide them the results.

This project require to Design 4 pages of MOLT:
• Public Home Page (Code - V01)
• Dashboard (private Home Page) (Code - V03)
• Monitor (web GIS) (Code - V14)
• Registration Page (Code - V04)

We would like to provide the required time to make a good job.

Target Market(s)

Humanitarian Agencies, Goverments

Coding

Coded - Design and coding required

Number of Pages Required

4 page

Font styles to use
Other font styles liked:
• see the manual attached

Requirements
Must have
• 4 pages. One Home, one form, one dashboard and one web map.
Nice to have
• Please read the attachment with all the detailed instructions

```html
<!DOCTYPE html>
<html lang="en">
<head>
<meta charset="utf-8">
<title>MOLT – Sign up</title>
<link href="https://fonts.googleapis.com/css2?family=Poppins:wght@400;500;600&display=swap" rel="stylesheet">
<style>
:root{
  --ink:#1c1b1f;
  --muted:#5f6368;
  --line:#79747e;
  --brand:#2a4f5b;
  --accent:#ff8682;
  --gold:#e9b530;
  --social:#5b6bd5;
  --rule:#d6d6d6;
  --bg:#ffffff;
}
*{box-sizing:border-box;margin:0;padding:0}
html,body{width:1200px;height:1200px;overflow:hidden;background:var(--bg)}
body{position:relative;font-family:"Poppins",sans-serif;color:var(--ink)}
.hero{position:absolute;left:89px;top:171px;width:461px;height:827px;border-radius:26px;overflow:hidden;
  background:linear-gradient(160deg,#020304 0%,#06080c 35%,#1b3a5c 55%,#3f6f9a 72%,#8fb0cc 86%,#3d6688 100%)}
.hero-dots{position:absolute;left:205px;bottom:26px;display:flex;gap:7px;align-items:center}
.hero-dots .active{width:27px;height:8px;border-radius:4px;background:var(--gold)}
.hero-dots .dot{width:8px;height:8px;border-radius:50%;background:#fff}
.brand{position:absolute;left:932px;top:126px;display:flex;align-items:center;gap:18px}
.brand-mark{width:44px;height:44px;border-radius:50%;border:2px solid var(--gold)}
.brand-name{font-size:30px;font-weight:400;letter-spacing:10px;color:var(--brand)}
h1{position:absolute;left:583px;top:172px;font-size:36px;font-weight:600;line-height:1.2}
.lead{position:absolute;left:584px;top:234px;font-size:14px;color:var(--muted)}
.field{position:absolute;height:47px;border:1px solid var(--line);border-radius:4px;display:flex;align-items:center;padding:0 13px;font-size:14.5px}
.field .label{position:absolute;top:-9px;left:9px;padding:0 4px;background:var(--bg);font-size:12.5px;line-height:16px}
.field .icon{position:absolute;right:10px;top:50%;transform:translateY(-50%)}
.pw{letter-spacing:1px;font-size:14px}
.group{position:absolute;left:584px;top:429px;width:536px;height:163px;border:1px solid var(--line);border-radius:4px}
.group .label{position:absolute;top:-9px;left:9px;padding:0 4px;background:var(--bg);font-size:12.5px;line-height:16px}
.consent{position:absolute;left:585px;top:749px;display:flex;align-items:center;gap:9px;font-size:12.5px;font-weight:500}
.consent .box{width:17px;height:17px;border:2px solid var(--ink);border-radius:2px}
.link{color:var(--accent)}
.cta{position:absolute;left:584px;top:801px;width:536px;height:40px;border-radius:4px;background:var(--brand);color:#fff;
  font-size:13px;font-weight:600;display:flex;align-items:center;justify-content:center}
.login{position:absolute;left:0;width:1704px;top:853px;text-align:center;font-size:13px;font-weight:500}
.divider{position:absolute;left:584px;top:905px;width:536px;display:flex;align-items:center;gap:14px;font-size:12.5px;color:#8a8a8a}
.divider::before,.divider::after{content:"";flex:1;height:1px;background:var(--rule)}
.social{position:absolute;top:957px;width:170px;height:47px;border:1px solid var(--social);border-radius:4px;display:flex;align-items:center;justify-content:center;font-size:13px;font-weight:500;color:var(--ink)}
</style>
</head>
<body>
  <div class="hero" role="img" aria-label="Photograph of a satellite with solar panels orbiting above Earth">
    <div class="hero-dots"><span class="active"></span><span class="dot"></span><span class="dot"></span></div>
  </div>

  <div class="brand"><span class="brand-mark"></span><span class="brand-name">MOLT</span></div>

  <h1>Sign up</h1>
  <p class="lead">Let’s get you all set up!</p>

  <div class="field" style="left:584px;top:294px;width:258px"><span class="label">First Name</span>ana.berg@postmail.net</div>
  <div class="field" style="left:862px;top:294px;width:258px"><span class="label">Last Name</span>ana.berg@postmail.net</div>
  <div class="field" style="left:584px;top:361px;width:258px"><span class="label">Email</span>ana.berg@postmail.net</div>
  <div class="field" style="left:862px;top:361px;width:258px"><span class="label">Phone Number</span>ana.berg@postmail.net</div>

  <div class="group"><span class="label">Organization</span></div>
  <div class="field" style="left:597px;top:469px;width:251px"><span class="label">Street Address</span>1234 Linden Strasse</div>
  <div class="field" style="left:856px;top:469px;width:251px"><span class="label">Postal Code</span>12345</div>
  <div class="field" style="left:597px;top:533px;width:251px"><span class="label">City</span>New York</div>
  <div class="field" style="left:856px;top:533px;width:251px;padding-left:16px;padding-bottom:6px">Country
    <svg class="icon" width="14" height="14" viewBox="0 0 14 14" style="right:16px;margin-top:-3px"><path d="M3 5l4 4 4-4" fill="none" stroke="#1c1b1f" stroke-width="1.8"/></svg>
  </div>

  <div class="field" style="left:584px;top:613px;width:536px"><span class="label">Password</span><span class="pw">•••••••••••••••••••••••••</span>
    <svg class="icon" width="20" height="20" viewBox="0 0 24 24"><path d="M2 12s4-7 10-7 10 7 10 7-4 7-10 7S2 12 2 12z" fill="none" stroke="#1c1b1f" stroke-width="2"/><circle cx="12" cy="12" r="3" fill="#1c1b1f"/><path d="M4 3l17 18" stroke="#1c1b1f" stroke-width="2"/></svg>
  </div>
  <div class="field" style="left:584px;top:680px;width:536px"><span class="label">Confirm Password</span><span class="pw">•••••••••••••••••••••••••</span>
    <svg class="icon" width="20" height="20" viewBox="0 0 24 24"><path d="M2 12s4-7 10-7 10 7 10 7-4 7-10 7S2 12 2 12z" fill="none" stroke="#1c1b1f" stroke-width="2"/><circle cx="12" cy="12" r="3" fill="#1c1b1f"/><path d="M4 3l17 18" stroke="#1c1b1f" stroke-width="2"/></svg>
  </div>

  <div class="consent"><span class="box"></span><span>I agree to all the <span class="link">Terms</span> and <span class="link">Privacy Policies</span></span></div>

  <div class="cta">Create account</div>
  <p class="login">Already have an account? <span class="link">Login</span></p>

  <div class="divider">Or Sign up with</div>

  <div class="social" style="left:584px">Chirp</div>
  <div class="social" style="left:767px">Findly</div>
  <div class="social" style="left:950px">Orchard</div>
</body>
</html>
```